IT Company based on Biology Business Needs a Professional Web Design

We need a professional business website design for a new company called 'Vast KELP'. We develop the machine learning solutions especially focused on deep learning algorithms for biology industry. Our initial product is a vision detection on biological images to help doctors diagnose the symptoms. We would like to see designs that use the color green.

Industry/Entity Type

Business

Number of Pages Required

5+ page

```html
<!DOCTYPE html>
<html lang="en">
<head>
<meta charset="utf-8">
<title>Vast KELP — Machine Learning Solutions</title>
<link rel="stylesheet" href="https://fonts.googleapis.com/css2?family=Open+Sans:wght@400;600;700&family=Raleway:wght@400;500;600&display=swap">
<style>
  :root {
    --green: #6cbf3f;
    --green-dark: #13893f;
    --ink: #222;
    --text: #444;
    --muted: #8a8a8a;
    --white: #fff;
    --footer-bg: #f3f4f5;
    --rule: #d9dbdd;
    --dark: #050808;
  }
  * { box-sizing: border-box; margin: 0; padding: 0; }
  html, body { width: 740px; height: 1200px; overflow: hidden; }
  body { position: relative; font-family: "Open Sans", sans-serif; color: var(--text); background: var(--white); }
  .abs { position: absolute; }

  /* Header */
  .site-header { position: absolute; left: 0; top: 0; width: 740px; height: 66px; background: var(--white); }
  .brand { position: absolute; display: flex; align-items: center; gap: 6px; font-family: "Raleway", sans-serif; font-weight: 500; color: var(--green); white-space: nowrap; }
  .brand-dot { border-radius: 50%; background: var(--green-dark); flex: none; }
  .site-header .brand { left: 28px; top: 17px; font-size: 22px; }
  .site-header .brand-dot { width: 18px; height: 18px; }
  .main-nav a { position: absolute; top: 30px; font-size: 8px; color: #333; text-decoration: none; letter-spacing: .2px; white-space: nowrap; }
  .main-nav a.active { color: var(--green-dark); }
  .main-nav a.active::after { content: ""; position: absolute; left: -4px; right: -4px; top: 14px; height: 2px; background: var(--green-dark); }

  /* Hero */
  .hero { position: absolute; left: 0; top: 66px; width: 740px; height: 315px; overflow: hidden; }
  .hero-image { position: absolute; inset: 0; background: radial-gradient(ellipse at 45% 60%, #5a7899 0%, #31506f 40%, #1a2f47 100%); }
  .hero-title { position: absolute; left: 156px; top: 60px; font-family: "Raleway", sans-serif; font-weight: 400; font-size: 88px; line-height: 1; color: var(--green); letter-spacing: 6px; }
  .hero-rule { position: absolute; left: 160px; top: 148px; width: 416px; height: 1px; background: rgba(255,255,255,.85); }
  .hero-sub { position: absolute; left: 160px; top: 154px; font-family: "Raleway", sans-serif; font-weight: 500; font-size: 36px; color: var(--white); letter-spacing: 2.4px; white-space: nowrap; }
  .slider-dots { position: absolute; left: 682px; top: 98px; width: 17px; height: 92px; border-radius: 9px; background: rgba(255,255,255,.25); }
  .slider-dots span { position: absolute; left: 5px; width: 7px; height: 7px; border-radius: 50%; background: var(--white); }
  .slider-dots span.on { background: var(--green); }

  /* Welcome */
  .welcome h1 { position: absolute; left: 0; width: 740px; top: 408px; text-align: center; font-family: "Raleway", sans-serif; font-weight: 400; font-size: 22px; color: var(--ink); }
  .welcome h1 em { font-style: normal; color: var(--green); font-weight: 500; }
  .welcome p { position: absolute; left: 62px; width: 616px; top: 451px; text-align: center; font-size: 7.2px; line-height: 12.8px; color: #555; }
  .btn { position: absolute; background: var(--green-dark); color: var(--white); font-size: 7.5px; text-align: center; text-decoration: none; }
  .welcome .btn { left: 330px; top: 503px; width: 75px; height: 23px; line-height: 23px; }

  /* Services */
  .services { position: absolute; left: 0; top: 564px; width: 740px; height: 411px; overflow: hidden; }
  .services-bg { position: absolute; inset: 0; background: radial-gradient(ellipse at 40% 35%, #1b2a28 0%, #0d1514 45%, var(--dark) 100%); }
  .services h2 { position: absolute; left: 0; width: 740px; top: 24px; text-align: center; font-family: "Raleway", sans-serif; font-weight: 400; font-size: 21px; color: var(--white); }
  .services h2 em { font-style: normal; color: var(--green); }
  .timeline { position: absolute; left: 365px; top: 68px; width: 1px; height: 272px; background: rgba(255,255,255,.35); }
  .service-icon { position: absolute; width: 70px; height: 70px; border-radius: 50%; border: 3px solid #e6e6e6; background: var(--green-dark); display: flex; align-items: center; justify-content: center; }
  .service-icon.light { background: var(--white); border-color: var(--green-dark); }
  .service { position: absolute; width: 218px; }
  .service h3 { font-family: "Raleway", sans-serif; font-weight: 600; font-size: 12.5px; color: var(--green); margin-bottom: 6px; }
  .service p { font-size: 6.9px; line-height: 12px; color: #e8e8e8; }
  .service .more { display: inline-block; margin-top: 4px; font-size: 6.8px; font-weight: 700; color: var(--white); }
  .service .more::after { content: ""; display: inline-block; margin-left: 5px; border-left: 3px solid var(--white); border-top: 2.5px solid transparent; border-bottom: 2.5px solid transparent; }
  .service.left { text-align: right; }

  /* Footer */
  .site-footer { position: absolute; left: 0; top: 975px; width: 740px; height: 166px; background: var(--footer-bg); }
  .site-footer .brand { left: 40px; top: 64px; font-size: 28px; }
  .site-footer .brand-dot { width: 22px; height: 22px; }
  .footer-col { position: absolute; top: 21px; height: 128px; border-left: 1px solid var(--rule); padding-left: 19px; }
  .footer-col h4 { font-family: "Raleway", sans-serif; font-weight: 500; font-size: 11px; color: #333; margin: 9px 0 7px; }
  .footer-col ul { list-style: none; }
  .footer-col li { font-size: 7px; color: var(--muted); line-height: 17.5px; position: relative; padding-left: 8px; }
  .footer-col li::before { content: ""; position: absolute; left: 0; top: 8px; width: 2px; height: 2px; border-radius: 50%; background: #aaa; }
  .bottom-bar { position: absolute; left: 0; top: 1141px; width: 740px; height: 59px; background: var(--green-dark); }
  .copyright { position: absolute; left: 0; width: 750px; top: 22px; text-align: center; font-size: 7px; color: var(--white); }
  .social { position: absolute; top: 19px; width: 18px; height: 18px; border: 1px solid var(--white); }
</style>
</head>
<body>

<header class="site-header">
  <div class="brand"><span class="brand-dot"></span>Vast KELP</div>
  <nav class="main-nav">
    <a class="active" style="left:242px">HOME</a>
    <a style="left:304px">ABOUT US</a>
    <a style="left:381px">SERVICE</a>
    <a style="left:451px">PRODUCT</a>
    <a style="left:526px">TESTIMONIALS</a>
    <a style="left:620px">CONTACT US</a>
  </nav>
</header>

<section class="hero">
  <div class="hero-image" role="img" aria-label="Blurred blue close-up of a DNA double helix"></div>
  <div class="hero-title">MACHINE</div>
  <div class="hero-rule"></div>
  <div class="hero-sub">LEARNING SOLUTIONS</div>
  <div class="slider-dots">
    <span style="top:7px"></span><span style="top:24px"></span><span class="on" style="top:42px"></span><span style="top:59px"></span><span style="top:76px"></span>
  </div>
</section>

<section class="welcome">
  <h1>Welcome to <em>VAST KELP</em></h1>
  <p>Lorem ipsum dolor sit amet, consectetur adipiscing elit, sed do eiusmod tempor incididunt ut labore et dolore magna aliqua. Ut enim ad minim veniam, quis nostrud exercitation ullamco laboris nisi ut aliquip ex ea commodo consequat. Duis aute irure dolor in reprehenderit in voluptate velit esse cillum dolore eu fugiat nulla pariatur. Excepteur sint occaecat cupidatat non proident, sunt in culpa qui officia deserunt mollit anim id est laborum.</p>
  <a class="btn">READ MORE</a>
</section>

<section class="services">
  <div class="services-bg" role="img" aria-label="Dark backdrop with a faint world map, stock figures, gears and a head profile"></div>
  <h2>Our <em>Service</em></h2>
  <div class="timeline"></div>

  <div class="service-icon light" style="left:395px;top:82px">
    <svg width="34" height="30" viewBox="0 0 34 30" fill="none" stroke="#13893f" stroke-width="2.4" stroke-linejoin="round">
      <rect x="11" y="2" width="11" height="10"/><rect x="3" y="16" width="11" height="10"/><rect x="19" y="16" width="11" height="10"/>
    </svg>
  </div>
  <div class="service" style="left:479px;top:81px">
    <h3>Drug Possession</h3>
    <p>Early stage companies have great ideas but often times cannot bootstrap themselves to profitability. Other companies have customers and revenue, but want to invest</p>
    <span class="more">READ MORE</span>
  </div>

  <div class="service-icon" style="left:266px;top:130px">
    <svg width="30" height="30" viewBox="0 0 30 30" fill="none" stroke="#fff" stroke-width="2.4">
      <circle cx="15" cy="15" r="12"/><polygon points="15,10 20,13.5 18,19 12,19 10,13.5" fill="#fff"/>
    </svg>
  </div>
  <div class="service left" style="left:40px;top:130px">
    <h3>Traffic Offenses</h3>
    <p>We have worked with both large and small internet companies, and have grown companies to become market leaders in their sectors. We understand the inner workings</p>
    <span class="more">READ MORE</span>
  </div>

  <div class="service-icon" style="left:396px;top:192px">
    <svg width="26" height="30" viewBox="0 0 26 30" fill="none" stroke="#fff" stroke-width="2.2" stroke-linejoin="round">
      <path d="M3 2h13l7 7v19H3z"/><path d="M16 2v7h7"/><path d="M8 15h10M8 19h10M8 23h10"/>
    </svg>
  </div>
  <div class="service" style="left:480px;top:192px">
    <h3>Fraud Offenses</h3>
    <p>We dedicate time on-site to our portfolio companies, and will arrange and attend key meetings with strategic partners or clients. Informal mentorship and advice through</p>
    <span class="more">READ MORE</span>
  </div>

  <div class="service-icon" style="left:266px;top:257px">
    <svg width="30" height="30" viewBox="0 0 30 30" fill="none" stroke="#fff" stroke-width="3" stroke-linecap="round">
      <path d="M7 7l16 16M23 7L7 23"/><circle cx="15" cy="15" r="4"/>
    </svg>
  </div>
  <div class="service left" style="left:40px;top:257px">
    <h3>Domestic violence</h3>
    <p>Harbor Ventures has key relationships in large web companies in Australia, the US, and the UK. These connections are critical to helping start the dialogue to create key</p>
    <span class="more">READ MORE</span>
  </div>
</section>

<footer class="site-footer">
  <div class="brand"><span class="brand-dot"></span>Vast KELP</div>
  <div class="footer-col" style="left:225px">
    <h4>Important Links</h4>
    <ul><li>Affiliate Program</li><li>Special Promotions</li><li>Newsletter</li><li>Contact</li></ul>
  </div>
  <div class="footer-col" style="left:398px">
    <h4>Categories</h4>
    <ul><li>Webmail Login</li><li>Account Login</li><li>FAQs</li><li>Server References</li></ul>
  </div>
  <div class="footer-col" style="left:570px">
    <h4>Navigation</h4>
    <ul><li>About Us</li><li>Services</li><li>News</li><li>product</li><li>Contact Us</li></ul>
  </div>
</footer>

<div class="bottom-bar">
  <p class="copyright">Copyright 2016 Company Name. &nbsp;All Rights Reserved.</p>
  <span class="social" style="left:634px"></span>
  <span class="social" style="left:661px"></span>
  <span class="social" style="left:687px"></span>
</div>

</body>
</html>
```